Mark Delavane

Early Voting is from October 20th through October 31st.

Locations: Civic Hall Bldg. 842 S. Wrenfield "Rear" Calder Springs, TX. 78650.

Campus Commons Bldg.
BKSC
3560 E. Marlow Dr.
Calder Springs, TX. 78650

Pol. Ad paid for by Candidate

if you can also include: A 20% tax exemption on your property for everyone. (this would go on the slogans he is using)

```html
<!DOCTYPE html>
<html lang="en">
<head>
<meta charset="utf-8">
<title>Mark Delavane for School Board Pl. 3 – Postcards</title>
<link href="https://fonts.googleapis.com/css2?family=Source+Sans+3:ital,wght@0,400;0,600;0,700;0,800;1,700;1,800;1,900&display=swap" rel="stylesheet">
<style>
  :root {
    --backdrop: #2b2b2b;
    --card: #ffffff;
    --red: #c8202b;
    --blue: #2e2f8f;
    --ink: #1a1a1a;
    --grey-line: #a9a9a9;
    --stamp: #f6e4dc;
    --photo-dark: #1d2440;
    --photo-light: #c79b84;
  }
  * { box-sizing: border-box; margin: 0; padding: 0; }
  html, body { width: 1200px; height: 1181px; overflow: hidden; }
  body {
    background: var(--backdrop);
    font-family: "Source Sans 3", Arial, sans-serif;
    position: relative;
  }
  .postcard {
    position: absolute;
    width: 800px;
    height: 517px;
    background: var(--card);
    overflow: hidden;
  }
  .postcard--mailer { left: 49px; top: 48px; }
  .postcard--front { left: 345px; top: 535px; }

  .elect-banner { position: absolute; left: 0; top: 0; width: 270px; height: 78px; }
  .elect-banner__word {
    position: absolute; left: 30px; top: 8px;
    font-size: 54px; font-weight: 800; font-style: italic;
    color: #fff; letter-spacing: 1px; line-height: 1;
  }
  .slogan {
    position: absolute; left: 232px;
    color: var(--red); font-weight: 700; font-style: italic;
    white-space: nowrap;
  }
  .slogan small { font-size: 0.68em; }
  .postcard--mailer .slogan { top: 48px; font-size: 22px; }
  .postcard--front .slogan { top: 38px; font-size: 30px; }

  .stamp-box {
    position: absolute; left: 680px; top: 20px;
    width: 102px; height: 101px; background: var(--stamp);
  }

  .name-panel {
    position: absolute; left: 29px; top: 90px;
    width: 427px; height: 192px;
    border: 1.5px solid var(--grey-line);
    overflow: hidden;
  }
  .candidate-name {
    color: var(--blue); font-weight: 800; line-height: 0.9;
  }
  .candidate-name span { display: block; }
  .district { color: var(--red); font-weight: 600; white-space: nowrap; }
  .seat { color: var(--blue); font-weight: 800; white-space: nowrap; }
  .seat small { font-size: 0.65em; font-weight: 600; }

  .name-panel .candidate-name { position: absolute; left: 10px; top: 26px; font-size: 58px; letter-spacing: -0.5px; }
  .name-panel .candidate-name span:first-child { font-size: 40px; font-weight: 600; padding-left: 32px; }
  .name-panel .district { position: absolute; left: 12px; top: 112px; font-size: 18px; }
  .name-panel .seat { position: absolute; left: 24px; top: 144px; font-size: 19px; }
  .name-panel .candidate-photo { position: absolute; left: 265px; top: 12px; width: 150px; height: 178px; }

  .candidate-photo {
    background: linear-gradient(180deg, var(--photo-light) 0%, var(--photo-light) 38%, var(--photo-dark) 40%, var(--photo-dark) 100%);
    border-radius: 60px 60px 0 0;
  }

  .about { position: absolute; left: 29px; top: 285px; font-size: 14.5px; line-height: 19px; color: var(--ink); }
  .early-voting {
    position: absolute; left: 27px; top: 413px;
    font-size: 20px; font-weight: 700; font-style: italic; color: var(--blue);
  }
  .social-link {
    position: absolute; left: 30px; top: 473px;
    font-size: 13.5px; color: var(--blue); display: flex; align-items: center; gap: 4px;
  }
  .social-link i { display: inline-block; width: 12px; height: 12px; background: var(--blue); }

  .tax-line {
    position: absolute; left: 36px; top: 90px;
    font-size: 38px; font-weight: 900; font-style: italic; color: var(--blue); white-space: nowrap;
  }
  .tax-line .accent { color: var(--red); }
  .tax-line .rest { font-size: 25px; font-weight: 400; font-style: normal; }
  .voting-dates { position: absolute; left: 36px; top: 140px; font-size: 22px; color: var(--ink); }

  .postcard--front .candidate-name { position: absolute; left: 80px; top: 178px; font-size: 106px; letter-spacing: -1px; }
  .postcard--front .candidate-name span:first-child { font-size: 70px; font-weight: 600; padding-left: 56px; }
  .postcard--front .district { position: absolute; left: 87px; top: 330px; font-size: 32px; }
  .postcard--front .seat { position: absolute; left: 108px; top: 383px; font-size: 33px; }
  .postcard--front .candidate-photo { position: absolute; left: 538px; top: 158px; width: 262px; height: 300px; border-radius: 110px 110px 0 0; }

  .footer-band { position: absolute; left: 0; bottom: 0; width: 800px; height: 100px; }
  .locations {
    position: absolute; left: 26px; top: 448px;
    font-size: 14.5px; line-height: 26px; color: #fff; white-space: nowrap;
  }
  .locations span { display: block; }
  .locations span + span { padding-left: 15px; }
  .disclaimer {
    position: absolute; right: 40px; top: 456px;
    font-size: 14.5px; line-height: 19px; color: #fff; text-align: right;
  }
</style>
</head>
<body>

  <section class="postcard postcard--mailer" aria-label="Mailer side">
    <svg class="elect-banner" viewBox="0 0 270 78" aria-hidden="true">
      <polygon points="0,0 260,0 200,64 0,64" fill="var(--red)"/>
      <polygon points="0,66 198,66 260,0 270,0 204,76 0,76" fill="var(--blue)"/>
    </svg>
    <div class="elect-banner__word">ELECT</div>
    <p class="slogan"><small>for</small> Students, <small>for</small> Teachers, <small>for</small> The Future...</p>
    <div class="stamp-box" aria-hidden="true"></div>

    <div class="name-panel">
      <h2 class="candidate-name"><span>Mark</span><span>Delavane</span></h2>
      <p class="district">Marlow CISD</p>
      <p class="seat"><small>for</small> SCHOOL BOARD Pl. 3</p>
      <div class="candidate-photo" role="img" aria-label="Portrait photo of the candidate in a dark suit and blue tie"></div>
    </div>

    <p class="about">About Mark<br>need some text</p>
    <p class="early-voting">Early Voting is from October 20th through October 31st.</p>
    <p class="social-link"><i aria-hidden="true"></i>Find me on Townsquare.</p>
  </section>

  <section class="postcard postcard--front" aria-label="Front side">
    <svg class="elect-banner" viewBox="0 0 270 78" aria-hidden="true">
      <polygon points="0,0 260,0 200,64 0,64" fill="var(--red)"/>
      <polygon points="0,66 198,66 260,0 270,0 204,76 0,76" fill="var(--blue)"/>
    </svg>
    <div class="elect-banner__word">ELECT</div>
    <p class="slogan"><small>for</small> Students, <small>for</small> Teachers, <small>for</small> The Future...</p>

    <p class="tax-line">A <span class="accent">20%</span> tax exemption <span class="rest">on your property for everyone</span></p>
    <p class="voting-dates">Voting is from October 20th through October 31st.</p>

    <div class="candidate-photo" role="img" aria-label="Portrait photo of the candidate smiling, in a dark suit and blue tie"></div>
    <h1 class="candidate-name"><span>Mark</span><span>Delavane</span></h1>
    <p class="district">Marlow CISD</p>
    <p class="seat"><small>for</small> SCHOOL BOARD Pl. 3</p>

    <svg class="footer-band" viewBox="0 0 800 100" preserveAspectRatio="none" aria-hidden="true">
      <path d="M0,18 C260,0 560,-4 800,20 L800,100 L0,100 Z" fill="var(--blue)"/>
      <path d="M560,4 C660,4 740,10 800,20 L800,100 L760,100 C740,70 700,40 600,12 Z" fill="var(--red)"/>
    </svg>
    <p class="locations">
      <span>Locations: Civic Hall Bldg. 842 S. Wrenfield "Rear" Calder Springs, TX. 78650</span>
      <span>Campus Commons Bldg. BKSC 3560 E. Marlow Dr. Calder Springs, TX. 78650</span>
    </p>
    <p class="disclaimer">Pol. Ad paid for<br>by Candidate</p>
  </section>

</body>
</html>
```